Business Card Design Competition

We need a business card design for our Internet Marketing company. We require both front and back designs and the final card must be 89x53mm in size, plus crop marks to 91x55mm. Colours as per logo, plus perhaps black and/or grey (#828282).
Final text must be editable (if you can supply an editable Fireworks PNG, even better)...
FRONT TEXT:
Full Name
Position
Address Line
Suburb, State, Postcode
Phone: 0000 000 000
Mobile: 0000 000 000
Email: xxx@brimleafpromo.com.au
Web: www.brimleafpromo.com.au
Rear of card should be a fresh design plus our slogan text: "Making You Stand Out" in large font, then in small text "Brimleaf Holdings Pty Ltd (ABN: 42 563 701 384)".
Target Market(s)
Small/Medium Businesses
Industry/Entity Type
Business
Look and feel
Each slider illustrates characteristics of the customer's brand and the style your logo design should communicate.

```html
<!DOCTYPE html>
<html lang="en">
<head>
<meta charset="utf-8">
<title>Brimleaf Promo – Business Card</title>
<link rel="stylesheet" href="https://fonts.googleapis.com/css2?family=PT+Sans:wght@400;700&display=swap">
<style>
  :root {
    --backdrop: #d9d9d6;
    --card-black: #000000;
    --card-white: #ffffff;
    --brand-green: #8dc63f;
    --brand-orange: #f7941d;
    --text-grey: #828282;
    --text-grey-dark: #6d6d6d;
  }
  * { margin: 0; padding: 0; box-sizing: border-box; }
  html, body {
    width: 1200px;
    height: 900px;
    overflow: hidden;
    background: var(--backdrop);
    font-family: "PT Sans", Arial, sans-serif;
  }
  .canvas { position: relative; width: 1200px; height: 900px; }

  .card {
    position: absolute;
    width: 628px;
    height: 374px;
    box-shadow: 0 3px 10px rgba(0,0,0,0.25);
  }

  /* Rear of card */
  .card--rear { left: 80px; top: 54px; background: var(--card-black); }
  .card--rear .brand {
    position: absolute;
    left: 40px;
    top: 72px;
    display: flex;
    align-items: center;
    gap: 14px;
  }
  .card--rear .brand-dot { width: 90px; height: 90px; }
  .card--rear .brand-name {
    font-size: 38px;
    font-weight: 400;
    color: var(--brand-green);
    line-height: 1;
  }
  .slogan {
    position: absolute;
    left: 146px;
    top: 180px;
    font-size: 23px;
    font-weight: 400;
    letter-spacing: 0.5px;
    text-transform: uppercase;
    color: var(--brand-orange);
  }
  .company-line {
    position: absolute;
    right: 14px;
    bottom: 26px;
    font-size: 14px;
    color: var(--text-grey);
  }

  /* Front of card */
  .card--front { left: 486px; top: 486px; background: var(--card-white); }
  .contact { position: absolute; left: 44px; top: 62px; color: var(--text-grey-dark); }
  .contact-name {
    font-size: 20px;
    font-weight: 400;
    text-transform: uppercase;
    color: var(--brand-orange);
    letter-spacing: 0.5px;
    line-height: 24px;
  }
  .contact-role { font-size: 16px; line-height: 22px; }
  .contact-details { margin-top: 14px; font-size: 16px; line-height: 22px; }
  .sep { padding: 0 6px; }

  .card--front .brand {
    position: absolute;
    right: 36px;
    top: 250px;
    display: flex;
    align-items: center;
    gap: 10px;
  }
  .card--front .brand-dot { width: 60px; height: 60px; }
  .card--front .brand-name {
    font-size: 24px;
    font-weight: 400;
    color: var(--brand-green);
    line-height: 1;
  }
  .web {
    position: absolute;
    right: 10px;
    bottom: 30px;
    font-size: 15px;
    color: var(--text-grey-dark);
  }
</style>
</head>
<body>
<main class="canvas">

  <section class="card card--rear" aria-label="Card rear">
    <div class="brand">
      <svg class="brand-dot" viewBox="0 0 90 90" aria-hidden="true">
        <circle cx="45" cy="45" r="43" fill="var(--brand-orange)"/>
      </svg>
      <span class="brand-name">Brimleaf Promo</span>
    </div>
    <p class="slogan">Making You Stand Out</p>
    <p class="company-line">Brimleaf Holdings Pty Ltd (ABN: 42 563 701 384)</p>
  </section>

  <section class="card card--front" aria-label="Card front">
    <div class="contact">
      <h1 class="contact-name">Daniel Harper</h1>
      <p class="contact-role">Vice President of Brimleaf Promo</p>
      <div class="contact-details">
        <p>58 Harbourview Lane<span class="sep">|</span>Carlton, VIC 3053</p>
        <p>P 0000 000 000<span class="sep">|</span>M 0000 000 000</p>
        <p>dharper@brimleafpromo.com.au</p>
      </div>
    </div>
    <div class="brand">
      <svg class="brand-dot" viewBox="0 0 60 60" aria-hidden="true">
        <circle cx="30" cy="30" r="28" fill="var(--brand-orange)"/>
      </svg>
      <span class="brand-name">Brimleaf Promo</span>
    </div>
    <p class="web">www.brimleafpromo.com.au</p>
  </section>

</main>
</body>
</html>
```